Wedding Invitations

We are a printing company "inkmorrow" and require multiple wedding invitation designs for our customers in store and online. We would like the designs to be editable in Photoshop if possible, if not then a layout with suggested fonts would be the next best option. We are open to suggestions on design but would like to stick to the general wedding themes some with a modern and some with a classical feel

Industry/Entity Type

Printing

```html
<!DOCTYPE html>
<html lang="en">
<head>
<meta charset="utf-8">
<title>Wedding Invitation — inkmorrow</title>
<link rel="stylesheet" href="https://fonts.googleapis.com/css2?family=Marcellus&family=EB+Garamond:ital,wght@1,500&display=swap">
<style>
  :root {
    --parchment-light: #e6c99a;
    --parchment-mid: #d2a96d;
    --parchment-dark: #a97b43;
    --ink: #2b1d12;
    --ornament-light: rgba(120, 90, 60, 0.18);
    --ornament-dark: rgba(80, 58, 38, 0.32);
  }
  html, body {
    margin: 0;
    padding: 0;
    overflow: hidden;
    background: #ffffff;
  }
  .invitation-card {
    position: relative;
    width: 1200px;
    height: 808px;
    overflow: hidden;
    background:
      radial-gradient(ellipse at 45% 40%, var(--parchment-light) 0%, var(--parchment-mid) 55%, var(--parchment-dark) 100%);
  }
  .ornament {
    position: absolute;
    top: 14px;
    width: 250px;
    height: 465px;
    border-radius: 40px;
    background: radial-gradient(ellipse at 50% 45%, var(--ornament-dark) 0%, var(--ornament-light) 55%, transparent 80%);
  }
  .ornament--left { left: 0; }
  .ornament--right { right: 0; }
  .invitation-title {
    position: absolute;
    top: 30px;
    left: 0;
    width: 1200px;
    margin: 0;
    text-align: center;
    padding-left: 0;
    transform: translateX(10px);
    font-family: "Marcellus", serif;
    font-weight: 400;
    font-size: 76px;
    letter-spacing: 12px;
    color: var(--ink);
  }
  .invitation-line {
    position: absolute;
    margin: 0;
    width: 800px;
    text-align: center;
    font-family: "EB Garamond", serif;
    font-style: italic;
    font-weight: 500;
    font-size: 31px;
    line-height: 1;
    color: var(--ink);
    transform: translateX(-50%);
    white-space: nowrap;
  }
</style>
</head>
<body>
  <main class="invitation-card">
    <div class="ornament ornament--left" role="img" aria-label="Vintage dress form with flourish scrollwork"></div>
    <div class="ornament ornament--right" role="img" aria-label="Vintage dress form with flourish scrollwork"></div>

    <h1 class="invitation-title">INVITATION</h1>

    <p class="invitation-line" style="left:582px; top:186px;">Mr. and Mrs. Alexander Whitford</p>
    <p class="invitation-line" style="left:565px; top:234px;">Hale</p>
    <p class="invitation-line" style="left:570px; top:283px;">request the honor of your presence</p>
    <p class="invitation-line" style="left:548px; top:331px;">at the marriage of their daughter</p>
    <p class="invitation-line" style="left:538px; top:382px;">Clara Jean</p>
    <p class="invitation-line" style="left:512px; top:426px;">to</p>
    <p class="invitation-line" style="left:565px; top:470px;">Mr. Thomas Edward Lane</p>
    <p class="invitation-line" style="left:565px; top:521px;">on Saturday, the fifth of August</p>
    <p class="invitation-line" style="left:562px; top:570px;">Nineteen hundred and ninety-four</p>
    <p class="invitation-line" style="left:548px; top:612px;">at two o'clock in the afternoon</p>
    <p class="invitation-line" style="left:540px; top:660px;">Saint Clement by-the-Bay</p>
    <p class="invitation-line" style="left:512px; top:709px;">Coral Cove, California</p>
  </main>
</body>
</html>
```